Kitesurf Weather Forecast Application Needs an Advertising Banner

We need an Advertising Banner for our iOS Kitesurf Weather Forecast Application. The application name is GustMapper and you can download it from the Plum Depot.

https://apps.plumdepot-market.com/app/gustmapper-breeze-and-sky-outlook/id804417392?mt=8

The banner should have the logo of our application, which can be either found from the Plum Depot or uploaded on this post. It should describe what our app does with either words or graphic story. GustMapper is a weather forecast application for Kitesurfers. As the banner is small, animated gifs will also be considered.

We need the following sizes 320x50 and 728x90. The banner will be uploaded to tavlo. Tavlo accepts images in PNG, JPEG and GIF. We want it in one of the formats that can be uploaded to TavLo and vector .ai so we can make changed if necessary in the future.

On tap the banner will open Plum Depot on the user's device and present GustMapper.

06/09. I added a screenshot from an application that the banner will be added. The screenshot is from an Lumafon 4 Max (it is from a big device). The red area on the bottom is where the advert will go and it should be readable.

Target Market(s)

Banner will be displayed in other iOS Applications. One of them is Rigging Reckoner https://apps.plumdepot-market.com/us/app/rigging-reckoner/id937206148?mt=8

Industry/Entity Type

Advertising

Font styles to use
Other font styles liked:
• San Francisco

Requirements
Must have
• GustMapper logo and communicate a clear message on what the application does. GustMapper is a weather forecast application for Kitesurfers. If you want to find more information please visit the PlumDepot link provided.
Nice to have
• Animated gif will be nice to have, as the banner is small and it maybe difficult to communicate the message required.
Should not have
• We prefer something minimal and along the lines of our application design.

```html
<!DOCTYPE html>
<html lang="en">
<head>
<meta charset="utf-8">
<title>GustMapper Banner</title>
<link href="https://fonts.googleapis.com/css2?family=Anton&family=Open+Sans:wght@400&display=swap" rel="stylesheet">
<style>
  :root {
    --ink: #2e2e2e;
    --accent: #f7941d;
    --sea: #1f7fa8;
    --sea-light: #4fa9cc;
    --paper: #ffffff;
  }
  html, body {
    margin: 0;
    padding: 0;
    width: 1200px;
    height: 148px;
    overflow: hidden;
    background: var(--paper);
  }
  .banner {
    position: relative;
    width: 1200px;
    height: 148px;
    background: var(--paper);
    overflow: hidden;
  }
  .waves {
    position: absolute;
    left: 0;
    bottom: 0;
    width: 780px;
    height: 80px;
    background: linear-gradient(180deg, var(--sea-light) 0%, var(--sea) 100%);
    border-top-right-radius: 40px;
  }
  .headline {
    position: absolute;
    left: 54px;
    top: 40px;
    margin: 0;
    font-family: "Anton", "Arial Narrow", sans-serif;
    font-weight: 400;
    font-size: 58px;
    line-height: 1;
    letter-spacing: -1px;
    color: var(--ink);
    text-transform: uppercase;
    transform: skewX(-14deg);
    transform-origin: left bottom;
    white-space: nowrap;
  }
  .headline .highlight { color: var(--accent); }
  .brand {
    position: absolute;
    left: 852px;
    top: 16px;
    display: flex;
    align-items: center;
    gap: 12px;
  }
  .brand-dot {
    width: 30px;
    height: 30px;
    border-radius: 50%;
    background: var(--ink);
  }
  .brand-name {
    font-family: "Open Sans", Arial, sans-serif;
    font-weight: 400;
    font-size: 42px;
    line-height: 1;
    color: var(--ink);
  }
  .download-button {
    position: absolute;
    left: 849px;
    top: 77px;
    width: 329px;
    height: 50px;
    background: var(--accent);
    color: var(--paper);
    font-family: "Open Sans", Arial, sans-serif;
    font-size: 33px;
    line-height: 50px;
    text-align: center;
    text-decoration: none;
  }
</style>
</head>
<body>
  <div class="banner">
    <div class="waves" role="img" aria-label="Stylised blue ocean waves illustration"></div>
    <h1 class="headline">Looking for perfect <span class="highlight">weather</span>?</h1>
    <div class="brand">
      <span class="brand-dot"></span>
      <span class="brand-name">GustMapper</span>
    </div>
    <a class="download-button" href="#">Download Now</a>
  </div>
</body>
</html>
```